PuraVeln

Hi, We are looking for a design Label for our Packaged Drinking Water. We want a label in rich color. The current Label is uploaded. We wish for a much brighter color rather than black. Our current label is in black. We have attached other company labels to give you idea. The Solmira bottle image is also uploaded they use sticker for their bottle, front sticker contains name and back sticker's inner portion has graphics and the outer side has information we also open to that.
Industry/Entity Type
Packaged Drinking Water Bottle Brand
Look and feel
Each slider illustrates characteristics of the customer's brand and the style your logo design should communicate.

```html
<!DOCTYPE html>
<html lang="en">
<head>
<meta charset="UTF-8">
<title>PuraVeln – Packaged Drinking Water Label</title>
<link href="https://fonts.googleapis.com/css2?family=Outfit:wght@400;600&display=swap" rel="stylesheet">
<style>
  :root {
    --canvas-bg: #e4e4e4;
    --label-light: #eef7f8;
    --label-mid: #c4e8ec;
    --label-aqua: #7ccfdb;
    --wash-deep: rgba(70, 178, 196, 0.55);
    --wash-soft: rgba(110, 200, 214, 0.45);
    --ink-teal: #0f5257;
    --mark-green: #1b8a3a;
    --mark-bg: #ffffff;
  }
  html, body {
    margin: 0;
    padding: 0;
    width: 1200px;
    height: 800px;
    overflow: hidden;
    background: var(--canvas-bg);
  }
  .canvas {
    position: relative;
    width: 1200px;
    height: 800px;
  }
  .label {
    position: absolute;
    left: 140px;
    top: 230px;
    width: 920px;
    height: 340px;
    overflow: hidden;
    background: linear-gradient(100deg, var(--label-light) 0%, var(--label-mid) 45%, var(--label-aqua) 100%);
    box-shadow: 0 6px 24px rgba(0,0,0,0.10);
  }
  .label__artwork {
    position: absolute;
    inset: 0;
    background:
      radial-gradient(ellipse 420px 200px at 640px 300px, var(--wash-deep) 0%, rgba(70,178,196,0) 100%),
      radial-gradient(ellipse 360px 160px at 300px 330px, var(--wash-soft) 0%, rgba(110,200,214,0) 100%),
      radial-gradient(ellipse 300px 140px at 820px 120px, rgba(255,255,255,0.35) 0%, rgba(255,255,255,0) 100%);
  }
  .label__veg-mark {
    position: absolute;
    right: 60px;
    top: 36px;
    width: 22px;
    height: 22px;
  }
  .brand {
    position: absolute;
    left: 70px;
    top: 120px;
  }
  .brand__name {
    margin: 0;
    font-family: "Outfit", sans-serif;
    font-weight: 600;
    font-size: 92px;
    line-height: 1;
    letter-spacing: 1px;
    color: var(--ink-teal);
  }
  .brand__tm {
    font-size: 18px;
    font-weight: 400;
    vertical-align: top;
    margin-left: 4px;
    position: relative;
    top: -4px;
  }
  .brand__descriptor {
    margin: 12px 0 0 6px;
    font-family: "Outfit", sans-serif;
    font-weight: 400;
    font-size: 17px;
    letter-spacing: 5px;
    text-transform: uppercase;
    color: var(--ink-teal);
  }
</style>
</head>
<body>
  <main class="canvas">
    <section class="label">
      <div class="label__artwork" role="img" aria-label="Line illustration of mountain peaks over a watercolour aqua wash"></div>

      <svg class="label__veg-mark" viewBox="0 0 22 22" aria-hidden="true">
        <rect x="1" y="1" width="20" height="20" fill="var(--mark-bg)" stroke="var(--mark-green)" stroke-width="2"/>
        <circle cx="11" cy="11" r="5" fill="var(--mark-green)"/>
      </svg>

      <div class="brand">
        <h1 class="brand__name">PuraVeln<span class="brand__tm">™</span></h1>
        <p class="brand__descriptor">Packaged Drinking Water</p>
      </div>
    </section>
  </main>
</body>
</html>
```